New Zealand Luggage Importer Needs Business Cards

We need professional, creative and fashionable business cards created.
We are based in New Zealand and import and distribute high-end, quality, fashionable and durable luggage.
We pride ourselves on selling the very best quality luggage, second only to 1 brand (which we won't mention here)...we use the same manufacturer. However, our prices are much more reasonable.
Business
Sam Ortiz
027 481 2956
3/17 Kestrel Lane, Morrow Flats, Auckland, 0614
PO Box 208354, North Shore, Auckland 0792
09-527-3061
sales@brindlecases.co.nz / www.brindlecases.co.nz

```html
<!DOCTYPE html>
<html lang="en">
<head>
<meta charset="utf-8">
<title>Brindle Cases — Business Cards</title>
<link rel="stylesheet" href="https://fonts.googleapis.com/css2?family=Michroma&family=Source+Sans+3:wght@400;600&display=swap">
<style>
  :root {
    --backdrop: #e4e4e4;
    --card-dark: #0b0b0c;
    --card-mid: #1d1d20;
    --ink-white: #f4f4f4;
    --ink-soft: #d6d6d6;
    --gold-light: #f3dc8c;
    --gold: #c99a3a;
    --gold-deep: #6e4d14;
    --rule-grey: #a7a7a9;
  }
  * { margin: 0; padding: 0; box-sizing: border-box; }
  html, body { width: 1200px; height: 852px; overflow: hidden; }
  body {
    background: var(--backdrop);
    position: relative;
    font-family: "Source Sans 3", Arial, sans-serif;
  }
  .card {
    position: absolute;
    width: 520px;
    height: 318px;
    border-radius: 18px;
    overflow: hidden;
    background: linear-gradient(160deg, var(--card-mid) 0%, var(--card-dark) 55%, #050505 100%);
    box-shadow: 0 8px 22px rgba(0,0,0,0.28);
  }
  .card--front { left: 60px; top: 130px; }
  .card--back { left: 620px; top: 404px; }

  .brand-name {
    font-family: "Michroma", "Arial Black", sans-serif;
    color: var(--ink-white);
    letter-spacing: 1px;
    white-space: nowrap;
    position: absolute;
  }
  .card--front .brand-name { font-size: 30px; left: 50%; top: 50%; transform: translate(-50%, -50%); }
  .card--back .brand-name { font-size: 27px; left: 92px; top: 58px; }

  .gold-strip {
    position: absolute; left: 0; top: 0; bottom: 0; width: 42px;
    background: linear-gradient(180deg, var(--gold-deep) 0%, var(--gold-light) 30%, var(--gold) 55%, var(--gold-light) 75%, var(--gold-deep) 100%);
  }
  .strip-edge {
    position: absolute; left: 42px; top: 0; bottom: 0; width: 5px;
    background: var(--rule-grey);
  }

  .person { position: absolute; left: 92px; top: 140px; }
  .person__name {
    font-family: "Michroma", "Arial Black", sans-serif;
    font-size: 17px; color: var(--ink-white); letter-spacing: 1px;
  }
  .person__title { font-size: 11px; color: var(--ink-soft); margin-top: 1px; }

  .contact { position: absolute; list-style: none; }
  .contact li {
    display: flex; align-items: center; gap: 9px;
    font-size: 12.5px; color: var(--ink-white); height: 17px; white-space: nowrap;
  }
  .contact svg { width: 11px; height: 11px; flex: none; }
  .contact--main { left: 92px; top: 196px; }
  .contact--web { left: 300px; top: 142px; }
</style>
</head>
<body>
  <section class="card card--front" aria-label="Card front">
    <div class="brand-name">BRINDLE CASES</div>
  </section>

  <section class="card card--back" aria-label="Card back">
    <div class="gold-strip"></div>
    <div class="strip-edge"></div>
    <div class="brand-name">BRINDLE CASES</div>

    <div class="person">
      <div class="person__name">SAM ORTIZ</div>
      <div class="person__title">Managing Director</div>
    </div>

    <ul class="contact contact--web">
      <li>
        <svg viewBox="0 0 12 12" aria-hidden="true"><rect x="0.5" y="2" width="11" height="8" fill="none" stroke="#c99a3a"/><path d="M0.5 2 L6 7 L11.5 2" fill="none" stroke="#c99a3a"/></svg>
        sales@brindlecases.co.nz
      </li>
      <li>
        <svg viewBox="0 0 12 12" aria-hidden="true"><circle cx="6" cy="6" r="5.3" fill="none" stroke="#c99a3a"/><ellipse cx="6" cy="6" rx="2.3" ry="5.3" fill="none" stroke="#c99a3a"/><path d="M0.7 6 H11.3" stroke="#c99a3a"/></svg>
        www.brindlecases.co.nz
      </li>
    </ul>

    <ul class="contact contact--main">
      <li>
        <svg viewBox="0 0 12 12" aria-hidden="true"><path d="M1 4 Q6 0 11 4 L10 5.5 L8 4.5 L8 3.8 Q6 3 4 3.8 L4 4.5 L2 5.5 Z" fill="#c99a3a"/><rect x="2.5" y="6.5" width="7" height="4.5" rx="1" fill="#c99a3a"/></svg>
        027 481 2956
      </li>
      <li>
        <svg viewBox="0 0 12 12" aria-hidden="true"><rect x="3" y="0.5" width="6" height="11" rx="1.2" fill="none" stroke="#c99a3a"/><circle cx="6" cy="9.6" r="0.7" fill="#c99a3a"/></svg>
        09-527-3061
      </li>
      <li>
        <svg viewBox="0 0 12 12" aria-hidden="true"><path d="M6 11.5 C3 7.5 2 6 2 4.3 A4 4 0 0 1 10 4.3 C10 6 9 7.5 6 11.5 Z" fill="#c99a3a"/><circle cx="6" cy="4.3" r="1.5" fill="#0b0b0c"/></svg>
        3/17 Kestrel Lane, Morrow Flats, Auckland, 0614
      </li>
      <li>
        <svg viewBox="0 0 12 12" aria-hidden="true"><rect x="0.5" y="4" width="11" height="5.5" rx="2.5" fill="#c99a3a"/><rect x="5.5" y="9" width="1.2" height="3" fill="#c99a3a"/><rect x="7.5" y="1" width="1" height="3.5" fill="#c99a3a"/><rect x="8.5" y="1" width="2.5" height="1.5" fill="#c99a3a"/></svg>
        PO Box 208354, North Shore, Auckland 0792
      </li>
    </ul>
  </section>
</body>
</html>
```